I need new business cards for my webb agency.

We need front AND backside.

Front:
Name, Title, company name, www, email, adress, phone 1, skype,

Back:
Logo + We will use promo text about what we do i.e. Web design, Search engine marketing, Advertisements & Web analytics

We want to look like a young and creative web agency. Business card should match our logo and colors. Please new this is a new logo enclosed which we are not using anywhere yet.

We will print on solid quality paper.

www.tarnlyworks.com

Rattanara Suites 10 th fl.
42/15 Phahonkit Soi 28
Bangkok 10110
Thailand
+66 (0) 2-487-6031

```html
<!DOCTYPE html>
<html lang="en">
<head>
<meta charset="utf-8">
<title>Tarnly Works – Business Card</title>
<link href="https://fonts.googleapis.com/css2?family=Open+Sans:wght@400;600;700&display=swap" rel="stylesheet">
<style>
  :root {
    --bg: #e6e6e4;
    --card-white: #f7f7f6;
    --card-brown: #2f1e17;
    --orange: #f0922b;
    --ink: #3a2a22;
    --text-light: #efe6df;
  }
  * { box-sizing: border-box; margin: 0; padding: 0; }
  html, body {
    width: 1200px; height: 900px; overflow: hidden;
    background: var(--bg);
    font-family: "Open Sans", Arial, sans-serif;
  }
  .stage {
    position: relative; width: 1200px; height: 900px;
  }
  .card {
    position: absolute; left: 250px; width: 700px; height: 400px;
    box-shadow: 0 6px 18px rgba(0,0,0,0.18);
  }
  /* Back side */
  .card-back {
    top: 35px; background: var(--card-white);
  }
  .brand-lockup {
    position: absolute; left: 90px; top: 150px;
    display: flex; align-items: center; gap: 18px;
  }
  .brand-dot {
    width: 56px; height: 56px; border-radius: 50%; background: var(--orange);
  }
  .brand-name {
    font-weight: 700; font-size: 52px; letter-spacing: 2px;
    color: var(--ink); text-transform: uppercase;
  }
  .services {
    position: absolute; left: 90px; top: 250px;
    font-size: 15px; color: var(--orange);
    display: flex; gap: 10px;
  }
  .services .sep { color: #b9b2ac; }

  /* Front side */
  .card-front {
    top: 465px; background: var(--card-brown); color: var(--text-light);
  }
  .front-mark {
    position: absolute; left: 40px; top: 0; width: 270px; height: 400px;
    display: flex; flex-direction: column; align-items: center; justify-content: center; gap: 18px;
  }
  .front-mark .brand-dot { width: 120px; height: 120px; }
  .front-mark .brand-name { font-size: 26px; color: var(--orange); letter-spacing: 1px; }
  .divider {
    position: absolute; left: 340px; top: 70px; width: 2px; height: 260px;
    background: var(--orange);
  }
  .contact {
    position: absolute; left: 375px; top: 78px;
    font-size: 14px; line-height: 1.45;
  }
  .contact .person {
    font-weight: 700; font-size: 20px; color: var(--orange);
    text-transform: uppercase; letter-spacing: 0.5px; line-height: 1.1;
  }
  .contact .role { font-size: 15px; margin-bottom: 22px; }
  .contact .block { margin-bottom: 22px; }
</style>
</head>
<body>
<main class="stage">
  <section class="card card-back" aria-label="Card back">
    <div class="brand-lockup">
      <span class="brand-dot"></span>
      <span class="brand-name">Tarnly Works</span>
    </div>
    <p class="services">
      <span>Search engine marketing</span><span class="sep">|</span>
      <span>Advertisements</span><span class="sep">|</span>
      <span>Web analytics</span>
    </p>
  </section>

  <section class="card card-front" aria-label="Card front">
    <div class="front-mark">
      <span class="brand-dot"></span>
      <span class="brand-name">Tarnly Works</span>
    </div>
    <div class="divider"></div>
    <div class="contact">
      <p class="person">Marten Holm</p>
      <p class="role">Manager</p>
      <div class="block">
        <p>Rattanara Suites 10 th fl.</p>
        <p>42/15 Phahonkit Soi 28 Bangkok 10110 Thailand</p>
      </div>
      <div class="block">
        <p>+66 (0) 2-487-6031</p>
        <p>+46 (0) 8412 590 27</p>
      </div>
      <div class="block">
        <p>info@tarnlyworks.com</p>
        <p>www.tarnlyworks.com</p>
      </div>
    </div>
  </section>
</main>
</body>
</html>
```